Morvela Aesthetic Doctor

I require an elegant, luxurious looking business card for my aesthetic business. I am a doctor and that will set me aside from competitors. I am planning to provide home and spa based treatments to clients with high expectations. I have attached my logo.

```html
<!DOCTYPE html>
<html lang="en">
<head>
<meta charset="utf-8">
<title>Morvela Aesthetic Doctor – Business Card</title>
<link rel="stylesheet" href="https://fonts.googleapis.com/css2?family=Roboto:wght@300;400;500;700&display=swap">
<style>
  :root {
    --stage: #5a5c60;
    --blue-light: #2bb0e8;
    --blue-deep: #1c68c2;
    --sky: #5bbbe8;
    --ink-grey: #8e9196;
    --text-grey: #7d8085;
    --white: #ffffff;
    --faint-ring: #eef1f5;
  }
  * { box-sizing: border-box; margin: 0; padding: 0; }
  html, body { width: 1200px; height: 1124px; overflow: hidden; }
  body {
    background: var(--stage);
    font-family: "Roboto", Arial, sans-serif;
    position: relative;
  }
  .card {
    position: absolute;
    left: 150px;
    width: 900px;
    height: 514px;
    overflow: hidden;
    box-shadow: 0 6px 18px rgba(0,0,0,0.35);
  }

  /* Front */
  .card-front {
    top: 36px;
    background: linear-gradient(135deg, var(--blue-light) 0%, #2a8fd8 50%, var(--blue-deep) 100%);
    color: var(--white);
  }
  .card-front .bg-ring {
    position: absolute; right: 40px; top: 30px;
    width: 300px; height: 300px; border-radius: 50%;
    border: 10px solid rgba(255,255,255,0.12);
  }
  .brand {
    position: absolute;
    display: flex; align-items: center; gap: 22px;
    font-weight: 300;
  }
  .brand-ring {
    width: 110px; height: 110px; border-radius: 50%;
    border: 3px solid currentColor; flex: none;
  }
  .brand-name { line-height: 1; }
  .brand-name .word { display: block; font-size: 84px; letter-spacing: 6px; }
  .brand-name .tag { display: block; font-size: 28px; letter-spacing: 5px; margin-top: 8px; }
  .card-front .brand { left: 180px; top: 120px; color: var(--white); }
  .services {
    position: absolute; left: 0; right: 0; top: 320px;
    text-align: center; font-size: 25px; font-weight: 400; line-height: 1.45;
  }
  .services .dot { margin: 0 8px; }

  /* Back */
  .card-back { top: 578px; background: var(--white); }
  .card-back .bg-ring {
    position: absolute; right: 70px; top: 150px;
    width: 360px; height: 360px; border-radius: 50%;
    border: 12px solid var(--faint-ring);
  }
  .edge-bar {
    position: absolute; right: 0; top: 112px;
    width: 26px; height: 40px; background: var(--sky);
  }
  .holder {
    position: absolute; right: 56px; top: 56px; text-align: right;
  }
  .holder-name { color: var(--sky); font-size: 30px; font-weight: 700; }
  .holder-name .post { font-size: 20px; font-weight: 500; margin-left: 4px; }
  .holder-title { color: var(--text-grey); font-size: 22px; font-weight: 400; margin-top: 4px; }
  .card-back .brand { left: 90px; top: 150px; color: var(--ink-grey); }
  .social { position: absolute; left: 270px; top: 300px; display: flex; gap: 18px; }
  .social span { width: 28px; height: 28px; border-radius: 50%; background: var(--sky); }
  .contacts { position: absolute; left: 260px; top: 348px; list-style: none; }
  .contacts li {
    display: flex; align-items: center; gap: 16px;
    color: var(--text-grey); font-size: 24px; font-weight: 300; height: 38px;
  }
  .contacts svg { width: 22px; height: 22px; fill: none; stroke: var(--sky); stroke-width: 2; }
  .contacts .hl { color: var(--sky); }
</style>
</head>
<body>

<section class="card card-front">
  <div class="bg-ring"></div>
  <div class="brand">
    <div class="brand-ring"></div>
    <div class="brand-name"><span class="word">MORVELA</span><span class="tag">AESTHETIC DOCTOR</span></div>
  </div>
  <div class="services">
    <p>Dermal injectables<span class="dot">•</span>Plasma facials<span class="dot">•</span>Microneedling</p>
    <p>Skin boosters<span class="dot">•</span>Excessive sweating</p>
    <p>Home and Spa Based Treatments</p>
  </div>
</section>

<section class="card card-back">
  <div class="bg-ring"></div>
  <div class="edge-bar"></div>
  <div class="holder">
    <p class="holder-name">Dr Elise Varnholt,<span class="post">MRCPCH MD</span></p>
    <p class="holder-title">Australasian Diploma of Aesthetic Medicine</p>
  </div>
  <div class="brand">
    <div class="brand-ring"></div>
    <div class="brand-name"><span class="word">MORVELA</span><span class="tag">AESTHETIC DOCTOR</span></div>
  </div>
  <div class="social"><span></span><span></span></div>
  <ul class="contacts">
    <li><svg viewBox="0 0 24 24"><path d="M5 3h4l2 5-2.5 1.5a11 11 0 0 0 6 6L16 13l5 2v4a2 2 0 0 1-2 2A16 16 0 0 1 3 5a2 2 0 0 1 2-2z"/></svg>0800 555 014</li>
    <li><svg viewBox="0 0 24 24"><rect x="3" y="5" width="18" height="14" rx="1"/><path d="M3 6l9 7 9-7"/></svg>elise@morvela.co.nz</li>
    <li><svg viewBox="0 0 24 24"><circle cx="12" cy="12" r="9"/><path d="M3 12h18M12 3c3 3 3 15 0 18M12 3c-3 3-3 15 0 18"/></svg>www.<span class="hl">morvela</span>.co.nz</li>
  </ul>
</section>

</body>
</html>
```